Multi-Line Insurance PPC Landing Page - Conversion optimized.

We have a PPC landing page used for the general population to get an insurance quote through an agent's site.

We'd like to improve the page for PPC traffic, make it more conversion friendly.

Site should be a single long page.

We will dynamically change the form and headlines on the page depending on what insurance "line" is being called. ie, Lift, Auto, Home, Business.

The enclosed AI file has all of the raw elements we need. We're looking to enhance the design and conversion ability.

Target Market(s)

General public needed insurance services.

Industry/Entity Type

Insurance Broker

Number of Pages Required

1 page

Font styles to use
Sans Serif

Requirements
Must have
• Form, agent picture, name, address.

```html
<!DOCTYPE html>
<html lang="en">
<head>
<meta charset="utf-8">
<title>Insurance Quote Landing Page</title>
<link href="https://fonts.googleapis.com/css2?family=Open+Sans:wght@400;600;700&display=swap" rel="stylesheet">
<style>
  :root{
    --green:#5a9a1f;
    --green-dark:#437a12;
    --green-btn:#62a327;
    --blue-head:#1d5a86;
    --teal:#2b86b3;
    --panel:#eef3f6;
    --agent-bg:#dfeef8;
    --text:#555d63;
    --muted:#7b848a;
    --field-border:#c9d2d8;
    --footer-dark:#2f5f10;
    --brand-red:#c8202f;
    --white:#ffffff;
  }
  *{box-sizing:border-box;margin:0;padding:0}
  html,body{width:681px;height:1200px;overflow:hidden}
  body{font-family:"Open Sans",Arial,sans-serif;color:var(--text);background:var(--white);position:relative}
  .hero{position:absolute;left:0;top:0;width:681px;height:232px;
    background:linear-gradient(180deg,#9ccbe8 0%,#cfe4ee 38%,#a9c47a 62%,#6f9a3e 100%)}
  .call-box{position:absolute;right:12px;top:10px;display:flex;align-items:center;gap:7px;
    background:rgba(29,90,134,.88);color:var(--white);padding:5px 10px;border-radius:3px}
  .call-box .label{font-size:9px;line-height:1}
  .call-box .number{font-size:15px;font-weight:700;line-height:1.1}
  .agent{position:absolute;left:0;top:232px;width:250px;height:240px;background:var(--agent-bg)}
  .agent-photo{position:absolute;left:26px;top:22px;width:88px;height:104px;
    background:linear-gradient(180deg,#c9d6df,#5d6e7c);border:2px solid var(--white)}
  .brand{position:absolute;left:26px;top:140px;font-size:17px;font-weight:700;color:var(--brand-red)}
  .agent-name{position:absolute;left:26px;top:166px;font-size:13px;font-weight:700;color:var(--blue-head)}
  .agent-role{font-weight:400}
  .agent-address{position:absolute;left:26px;top:185px;font-size:8px;color:var(--muted)}
  .agent-phone{position:absolute;left:26px;top:203px;font-size:13px;font-weight:700;color:var(--blue-head);display:flex;align-items:center;gap:5px}
  .quote{position:absolute;left:250px;top:232px;width:431px;height:240px;background:var(--panel)}
  .quote h1{text-align:center;margin-top:12px;font-size:13px;font-weight:600;color:var(--blue-head);line-height:1.35}
  .form{position:absolute;left:14px;top:58px;width:405px;display:grid;grid-template-columns:195px 195px;column-gap:15px;row-gap:10px}
  .field{height:24px;border:1px solid var(--field-border);background:var(--white);font-size:8px;color:var(--muted);padding:0 6px;display:flex;align-items:center;justify-content:space-between}
  .dob{display:flex;gap:5px}
  .dob .field{flex:1}
  .caret{font-size:6px}
  .btn{display:inline-block;background:var(--green-btn);color:var(--white);font-weight:600;border-radius:3px;text-align:center}
  .quote .btn{position:absolute;left:158px;top:200px;width:115px;height:26px;line-height:26px;font-size:11px}
  .intro{position:absolute;left:40px;top:497px;width:601px;text-align:center}
  .intro h2{font-size:12.5px;font-weight:700;color:var(--blue-head)}
  .intro p{font-size:11px;font-weight:600;color:var(--teal);margin-top:4px;line-height:1.35}
  .intro .next{color:var(--blue-head);font-weight:700}
  .services{position:absolute;left:22px;top:585px;width:637px;display:grid;grid-template-columns:repeat(3,1fr);column-gap:18px;row-gap:34px}
  .service{text-align:center;height:236px;position:relative}
  .service svg{display:block;margin:0 auto}
  .service h3{font-size:12px;font-weight:600;color:var(--blue-head);margin-top:8px}
  .service p{font-size:8px;line-height:1.45;margin-top:6px;padding:0 8px;color:var(--text)}
  .service .btn{position:absolute;left:50%;bottom:0;transform:translateX(-50%);width:86px;height:24px;line-height:24px;font-size:10px}
  .footer{position:absolute;left:0;top:1112px;width:681px;height:88px;background:var(--green);color:var(--white);text-align:center}
  .footer .built{font-size:8px;padding-top:9px;line-height:1.4}
  .footer nav{font-size:8px;margin-top:6px;display:flex;justify-content:center;gap:14px}
  .footer .legal{position:absolute;bottom:0;left:0;width:100%;height:22px;line-height:22px;background:var(--footer-dark);font-size:7.5px}
</style>
</head>
<body>
  <header class="hero" role="img" aria-label="Photo of a smiling family outdoors on a sunny lawn">
    <div class="call-box">
      <svg width="16" height="16" viewBox="0 0 24 24" aria-hidden="true"><path fill="#fff" d="M6.6 10.8a15 15 0 0 0 6.6 6.6l2.2-2.2c.3-.3.7-.4 1-.2 1.1.4 2.3.6 3.6.6.6 0 1 .4 1 1V20c0 .6-.4 1-1 1A17 17 0 0 1 3 4c0-.6.4-1 1-1h3.5c.6 0 1 .4 1 1 0 1.3.2 2.5.6 3.6.1.3 0 .7-.2 1z"/></svg>
      <div><div class="label">Call Us Today</div><div class="number">1300 555 014</div></div>
    </div>
  </header>

  <aside class="agent">
    <div class="agent-photo" role="img" aria-label="Portrait of the insurance agent"></div>
    <div class="brand">Harbor Mutual</div>
    <div class="agent-name">Owen Carter <span class="agent-role">- Agent</span></div>
    <div class="agent-address">4820 Sample Ave Los Angeles, CA 90012</div>
    <div class="agent-phone">
      <svg width="12" height="12" viewBox="0 0 24 24" aria-hidden="true"><path fill="currentColor" d="M6.6 10.8a15 15 0 0 0 6.6 6.6l2.2-2.2c.3-.3.7-.4 1-.2 1.1.4 2.3.6 3.6.6.6 0 1 .4 1 1V20c0 .6-.4 1-1 1A17 17 0 0 1 3 4c0-.6.4-1 1-1h3.5c.6 0 1 .4 1 1 0 1.3.2 2.5.6 3.6.1.3 0 .7-.2 1z"/></svg>
      123-555-0142
    </div>
  </aside>

  <section class="quote">
    <h1>Get an instant life insurance quote.<br>A fast and secure way to get a quote quickly.</h1>
    <div class="form">
      <div class="field">Full Name</div>
      <div class="field">Height / Weight <span class="caret">▼</span></div>
      <div class="field">Select Sex <span class="caret">▼</span></div>
      <div class="field">Select Tobacco Use <span class="caret">▼</span></div>
      <div class="dob">
        <div class="field">Month <span class="caret">▼</span></div>
        <div class="field">Day <span class="caret">▼</span></div>
        <div class="field">Year <span class="caret">▼</span></div>
      </div>
      <div class="field">Mobile Number</div>
      <div class="field">Select Current Health <span class="caret">▼</span></div>
      <div class="field">Email Address</div>
    </div>
    <span class="btn">Show The Quote</span>
  </section>

  <section class="intro">
    <h2>We cover all your insurance needs at the best prices, guaranteed.</h2>
    <p>Tailoring insurance coverage around your needs is easier than you think. We're here to help you learn more about all your options and provide answers to common questions. <span class="next">Ready to take the next step?</span></p>
  </section>

  <section class="services">
    <article class="service">
      <svg width="44" height="44" viewBox="0 0 44 44" aria-hidden="true"><circle cx="22" cy="22" r="20" fill="none" stroke="#1d5a86" stroke-width="2"/><path d="M12 25h20v-4l-3-5H15l-3 5z" fill="none" stroke="#1d5a86" stroke-width="2"/><circle cx="16" cy="27" r="2" fill="#1d5a86"/><circle cx="28" cy="27" r="2" fill="#1d5a86"/></svg>
      <h3>Auto Insurance</h3>
      <p>Get the protection you need at a price you can afford. Our agents compare coverage options, explain discounts you may qualify for, and help you build a policy that fits your car, your driving habits and your monthly budget without surprises.</p>
      <span class="btn">Get A Quote!</span>
    </article>
    <article class="service">
      <svg width="44" height="44" viewBox="0 0 44 44" aria-hidden="true"><circle cx="22" cy="22" r="20" fill="none" stroke="#1d5a86" stroke-width="2"/><path d="M11 22l11-9 11 9M14 20v10h16V20" fill="none" stroke="#1d5a86" stroke-width="2"/></svg>
      <h3>Home Insurance</h3>
      <p>Whether you own or rent, live in a new house or an older one, we help you protect the place you call home. Bundle your home and auto coverage and you may save more while keeping one simple point of contact.</p>
      <span class="btn">Get A Quote!</span>
    </article>
    <article class="service">
      <svg width="44" height="44" viewBox="0 0 44 44" aria-hidden="true"><circle cx="22" cy="22" r="20" fill="none" stroke="#1d5a86" stroke-width="2"/><path d="M22 31s-9-5.5-9-11a4.5 4.5 0 0 1 9-1 4.5 4.5 0 0 1 9 1c0 5.5-9 11-9 11z" fill="none" stroke="#1d5a86" stroke-width="2"/></svg>
      <h3>Life Insurance</h3>
      <p>We can help you find coverage that's right for you and your loved ones, including term and permanent plans. Our easy planning tools help you understand your options and figure out how much protection your family may need.</p>
      <span class="btn">Get A Quote!</span>
    </article>
    <article class="service">
      <svg width="44" height="44" viewBox="0 0 44 44" aria-hidden="true"><circle cx="22" cy="22" r="20" fill="none" stroke="#1d5a86" stroke-width="2"/><path d="M19 13h6v6h6v6h-6v6h-6v-6h-6v-6h6z" fill="none" stroke="#1d5a86" stroke-width="2"/></svg>
      <h3>Health Insurance</h3>
      <p>As your life changes, your health coverage should keep up. We help you compare individual and family plans, understand deductibles and networks, and choose a policy that gives you the care you need at a cost that works.</p>
      <span class="btn">Get A Quote!</span>
    </article>
    <article class="service">
      <svg width="44" height="44" viewBox="0 0 44 44" aria-hidden="true"><circle cx="22" cy="22" r="20" fill="none" stroke="#1d5a86" stroke-width="2"/><rect x="12" y="17" width="20" height="13" fill="none" stroke="#1d5a86" stroke-width="2"/><path d="M18 17v-3h8v3" fill="none" stroke="#1d5a86" stroke-width="2"/></svg>
      <h3>Business Insurance</h3>
      <p>Your business means everything to you, and protecting it matters to us. Whether you run a shop, an office or a crew on the road, we tailor coverage for property, liability and staff so you can focus on growth.</p>
      <span class="btn">Get A Quote!</span>
    </article>
    <article class="service">
      <svg width="44" height="44" viewBox="0 0 44 44" aria-hidden="true"><circle cx="22" cy="22" r="20" fill="none" stroke="#1d5a86" stroke-width="2"/><path d="M22 12l9 4v6c0 5-4 9-9 10-5-1-9-5-9-10v-6z" fill="none" stroke="#1d5a86" stroke-width="2"/></svg>
      <h3>Disability Insurance</h3>
      <p>These plans are designed to help replace part of your income if an illness or injury keeps you from working. Coverage helps protect your savings and keeps everyday bills paid while you focus on getting well again.</p>
      <span class="btn">Get A Quote!</span>
    </article>
  </section>

  <footer class="footer">
    <div class="built">This landing page built for:<br>Owen Carter - Agent | 4820 Sample Ave Los Angeles, CA 90012<br>123-555-0142</div>
    <nav><span>Auto Insurance</span><span>Home Insurance</span><span>Life Insurance</span><span>Health Insurance</span><span>Business Insurance</span><span>Disability Insurance</span></nav>
    <div class="legal">© 2013 CoverPoint Agents. All Rights Reserved. Privacy Policy | Terms &amp; Conditions</div>
  </footer>
</body>
</html>
```